Joomla Responsive Website Template for an International Biotechnology Company

Our client is a biotechnology company that uses silver-based technology to help make products antimicrobial, antibacterial, and anti fungal. We need a Joomla-based template that is responsive/mobile friendly when viewed on tablets or smartphones. We are looking for a template design for the home page and subpages. We are replacing the current website http://www.velmora-labs.com with a new website being built here: http://velmoraclean.com.stagehost.com/velmoraprime/. What we have now on the site is the basic wire frame. This is the desired layout and pictures we want to use. We would like you to add some design elements to make the website more professional looking and polished. Please refer to the attached style guide to help you in choosing the color. The client does like the green leaf, which is included in the last page of style guide and may be good for a background image. While the Velmora logo and leaf are green, we do not want to overuse the color green. The client does own other technologies that we will be promoting on the site and the logos for these technologies are attached below. These logos are Tusk, Velmora-Prime, and Wisp. We will be using this website to promote the technologies, the markets the technologies serve; drinking water, medical devices, apparel and textiles, and architectural surfaces, and to promote the customer using these devices. Please make the design "clean" and not cluttered, as these technologies are used to fight "dirty things".
Updates

Hello Designers! Thank you all very much for your design submissions. They were simply excellent. Due to the Holidays and New Years, many of the client's team members have been on vacation. We expect to have feedback shortly and pick the top design soon there after. Again, thank you all very much and hope the New Year brings you continued success. Best, Dorian

Industry/Entity Type

Biotechnology

Coding

Coded - Design and coding required

```html
<!DOCTYPE html>
<html lang="en">
<head>
<meta charset="utf-8">
<title>Velmora – Keeping the worlds surface safe</title>
<link rel="stylesheet" href="https://fonts.googleapis.com/css2?family=Open+Sans:wght@400;600;700&family=Arimo:wght@400;700&display=swap">
<style>
:root{
  --green:#7dc242;
  --blue:#0a5ca8;
  --blue-light:#1e90e0;
  --ink:#111;
  --grey:#9a9a9a;
  --leaf-1:#e9f3df;
  --leaf-2:#cfe6b8;
  --white:#fff;
}
*{margin:0;padding:0;box-sizing:border-box}
html,body{width:942px;height:1200px;overflow:hidden;background:var(--white)}
body{position:relative;font-family:"Open Sans",Arial,sans-serif;color:var(--ink)}
.abs{position:absolute}

/* header */
.hero{left:0;top:0;width:942px;height:313px;background:linear-gradient(160deg,#f7fbf3 0%,var(--leaf-1) 45%,var(--leaf-2) 100%)}
.brand{left:166px;top:22px;font-size:50px;font-weight:700;color:var(--green);letter-spacing:-1px;line-height:60px}
.contact-top{top:20px;font-size:12px;display:flex;align-items:center;gap:6px;white-space:nowrap}
.search{left:498px;top:62px;width:213px;height:26px;background:var(--green);color:var(--white);font-size:14px;font-weight:600;padding:4px 10px;display:flex;justify-content:space-between;align-items:center}
.menu-btn{left:752px;top:60px;width:27px;height:29px;background:var(--blue-light);border-radius:4px;display:flex;flex-direction:column;justify-content:center;align-items:center;gap:3px}
.menu-btn span{display:block;width:16px;height:3px;background:var(--white)}
.illustration{left:114px;top:92px;width:136px;height:170px;border-radius:6px;background:linear-gradient(160deg,rgba(214,120,120,.28),rgba(214,160,150,.12))}
.tagline{left:256px;top:162px;width:240px}
.tagline h1{font-size:15px;font-weight:700;margin-bottom:6px;white-space:nowrap}
.tagline p{font-size:10px;line-height:16px;color:#8a958a}
.login{left:498px;top:119px;width:199px;height:176px;background:var(--blue);border-radius:3px;padding:0 17px}
.login h2{color:var(--white);font-size:14px;font-weight:600;margin:11px 0 16px;white-space:nowrap;letter-spacing:-.2px}
.field{height:23px;background:var(--white);font-size:10px;color:var(--grey);padding:5px 9px;margin-bottom:20px}
.login-btn{width:88px;height:26px;margin:-2px auto 0;background:var(--green);color:var(--white);font-size:14px;font-weight:600;text-align:center;line-height:26px;border-radius:2px}

/* technologies */
.tech{left:0;top:313px;width:942px;height:126px;background:linear-gradient(180deg,#7dc242,#6db739)}
.tech h2{position:absolute;top:15px;width:100%;text-align:center;color:var(--white);font-size:15px;font-weight:700}
.tech-logo{top:46px;width:168px;height:56px;background:var(--white);border:2px solid var(--ink);display:flex;align-items:center;justify-content:center;font-size:22px;font-weight:700}

/* markets */
.market-img{width:129px;height:118px;border:2px solid var(--blue)}
.market-title{font-size:12.5px;font-weight:600;color:var(--blue);width:150px;white-space:nowrap}
.market-text{font-size:9.5px;line-height:12.6px;color:var(--grey);width:145px;margin-top:4px}
.view{width:63px;height:21px;background:var(--green);color:var(--white);font-size:12px;font-weight:700;text-align:center;line-height:21px;border-radius:2px}

/* news */
.news{left:0;top:776px;width:942px;height:175px;background:var(--blue);color:var(--white)}
.news h2{position:absolute;top:22px;width:100%;text-align:center;font-size:15px;font-weight:600}
.news-item{left:213px;top:70px;width:540px}
.news-item h3{font-size:13px;font-weight:600}
.news-item .date{font-size:10px;margin:6px 0 5px}
.news-item p{font-size:9.4px;line-height:16px;color:#cfe0f2;white-space:nowrap}
.arrow{top:89px;width:25px;height:25px;border-radius:50%;background:#c9d8e8;display:flex;align-items:center;justify-content:center}

/* footer */
.footer{font-family:Arimo,Arial,sans-serif}
.footer h4{font-size:13.5px;font-weight:400;color:var(--ink);white-space:nowrap}
.links{list-style:none;margin-top:9px}
.links li{font-family:"Open Sans",Arial,sans-serif;font-size:10px;line-height:13px;color:var(--grey);margin-bottom:8px;padding-left:14px;position:relative;white-space:nowrap}
.links li::before{content:"";position:absolute;left:2px;top:5px;width:4px;height:4px;border-radius:50%;background:#555}
.email{width:150px;height:22px;background:#a8aaa6;color:#555;font-size:11px;padding:4px 6px;margin-top:8px}
.subscribe{width:80px;height:23px;background:var(--green);color:var(--white);font-size:11px;text-align:center;line-height:23px;margin:12px 0 0 70px}
.social{display:flex;gap:10px;margin-top:8px}
.social span{width:24px;height:24px;background:var(--blue);border-radius:2px}
.contact-info{font-family:"Open Sans",Arial,sans-serif;font-size:10px;line-height:21px;color:var(--grey);margin-top:6px;white-space:nowrap}
.map{left:648px;top:980px;width:104px;height:113px;border:2px solid #333;background:linear-gradient(135deg,#e8e2cc,#d9d3bb)}
.bottom{left:0;top:1154px;width:942px;height:46px;background:var(--green);text-align:center;line-height:46px;font-family:Arimo,Arial,sans-serif;font-size:13px;color:#4b6a30}
</style>
</head>
<body>

<section class="abs hero" role="img" aria-label="Soft green leaf background"></section>
<div class="abs brand">velmora</div>

<div class="abs contact-top" style="left:513px">
  <svg width="10" height="10" viewBox="0 0 10 10"><path d="M2 0.5 L3.8 2.6 L2.8 3.8 Q4 6.3 6.2 7.2 L7.4 6.2 L9.5 8 L8 9.5 Q2.5 9 0.5 2 Z" fill="#1e90e0"/></svg>
  +91-555-010-2040
</div>
<div class="abs contact-top" style="left:635px">
  <svg width="12" height="9" viewBox="0 0 12 9"><rect x="0.5" y="0.5" width="11" height="8" fill="none" stroke="#1e90e0"/><path d="M0.5 0.5 L6 5 L11.5 0.5" fill="none" stroke="#1e90e0"/></svg>
  velmoraproducts@info.com
</div>

<div class="abs search">Search
  <svg width="14" height="14" viewBox="0 0 14 14"><circle cx="6" cy="6" r="4.5" fill="none" stroke="#fff" stroke-width="2"/><line x1="9.3" y1="9.3" x2="13" y2="13" stroke="#fff" stroke-width="2"/></svg>
</div>
<div class="abs menu-btn"><span></span><span></span><span></span></div>

<div class="abs illustration" role="img" aria-label="Molecule illustration"></div>
<div class="abs tagline">
  <h1>Keeping the worlds surface safe</h1>
  <p>Velmora branded antimicrobial technology makes products cleaner and longer lasting with silver, copper and zinc, which have been proven in use throughout history.</p>
</div>

<form class="abs login">
  <h2>VELMORA MEMBERS LOGIN</h2>
  <div class="field">user name</div>
  <div class="field">password</div>
  <div class="login-btn">LOGIN</div>
</form>

<section class="abs tech">
  <h2>OUR RELATED TECHNOLOGY</h2>
  <div class="abs tech-logo" style="left:192px;font-size:19px">VELMORA-PRIME</div>
  <div class="abs tech-logo" style="left:387px;color:#1e7fcf">WISP</div>
  <div class="abs tech-logo" style="left:583px;color:#d42a2a">TUSK</div>
</section>

<section class="markets">
  <div class="abs market-img" style="left:164px;top:468px;background:linear-gradient(90deg,#d9b39e,#eef2f4)" role="img" aria-label="Person drinking a glass of water"></div>
  <div class="abs" style="left:310px;top:466px">
    <div class="market-title">DRINKING WATER</div>
    <div class="market-text">It is a long established fact that a reader will be distracted by the readable content of a page when looking at its layout.</div>
  </div>
  <div class="abs view" style="left:380px;top:565px">VIEW</div>

  <div class="abs market-img" style="left:500px;top:468px;background:linear-gradient(180deg,#dfe6ea,#a9b7c0)" role="img" aria-label="Hospital room with medical equipment"></div>
  <div class="abs" style="left:646px;top:466px">
    <div class="market-title">MEDICAL EQUIPMENT</div>
    <div class="market-text">It is a long established fact that a reader will be distracted by the readable content of a page when looking at its layout.</div>
  </div>
  <div class="abs view" style="left:717px;top:565px">VIEW</div>

  <div class="abs market-img" style="left:164px;top:624px;background:linear-gradient(180deg,#5a5a60,#2d3f6e 55%,#2f68b8)" role="img" aria-label="Stacked folded fabrics"></div>
  <div class="abs" style="left:310px;top:622px">
    <div class="market-title">APPAREL &amp; TEXTILE</div>
    <div class="market-text">It is a long established fact that a reader will be distracted by the readable content of a page when looking at its layout.</div>
  </div>
  <div class="abs view" style="left:380px;top:721px">VIEW</div>

  <div class="abs market-img" style="left:500px;top:624px;background:linear-gradient(180deg,#e9eaea,#b8bcbc)" role="img" aria-label="Laboratory with clean work surfaces"></div>
  <div class="abs" style="left:646px;top:622px">
    <div class="market-title">ARCHITEC SURFACES</div>
    <div class="market-text">It is a long established fact that a reader will be distracted by the readable content of a page when looking at its layout.</div>
  </div>
  <div class="abs view" style="left:717px;top:721px">VIEW</div>
</section>

<section class="abs news">
  <h2>Our Latest VELMORA News</h2>
  <div class="abs arrow" style="left:158px"><svg width="10" height="12" viewBox="0 0 10 12"><path d="M7 1 L2 6 L7 11" fill="none" stroke="#0a5ca8" stroke-width="1.5"/></svg></div>
  <div class="abs news-item">
    <h3>Neque porro quisquam est</h3>
    <div class="date">25 November,2014</div>
    <p>It is a long established fact that a reader will be distracted by the readable content of a page when looking at its layout.<br>The point of using Lorem Ipsum is that it has a more-or-less normal distribution of letters</p>
  </div>
  <div class="abs arrow" style="left:760px"><svg width="10" height="12" viewBox="0 0 10 12"><path d="M3 1 L8 6 L3 11" fill="none" stroke="#0a5ca8" stroke-width="1.5"/></svg></div>
</section>

<footer class="footer">
  <div class="abs" style="left:187px;top:970px">
    <h4>Important Links</h4>
    <ul class="links">
      <li>Home</li><li>About Us</li><li>Markets</li><li>Technology</li><li>Customer Programs</li><li>News Highlights</li><li>Contact Us</li>
    </ul>
  </div>
  <div class="abs" style="left:325px;top:970px">
    <h4>Sign Up For Newsletter</h4>
    <div class="email">Your E-Mail</div>
    <div class="subscribe">SUBSCRIBE</div>
    <h4 style="margin-top:26px">Follow Us</h4>
    <div class="social">
      <span role="img" aria-label="Social link"></span><span role="img" aria-label="Social link"></span><span role="img" aria-label="Social link"></span><span role="img" aria-label="Social link"></span>
    </div>
  </div>
  <div class="abs" style="left:508px;top:970px">
    <h4>Contact Us</h4>
    <div class="contact-info">H.No:Lorem Ipsum is,<br>dummy text of the,<br>printing.<br>Phone: +123-555-0188<br>Email: Info@VELMORA.com</div>
  </div>
  <div class="abs map" role="img" aria-label="Location map"></div>
  <div class="abs bottom">All Rights Reserved.2014 VELMORA.com</div>
</footer>

</body>
</html>
```